8x8 Flyer - Holiday Party

Pinecrest Harbor Realty Group & Bluewater Lending Services, Inc.
Present Our
Annual Holiday Celebration

for Agents, Originators, Clients & Friends
All are Welcome!!

Catered by Chef Ra Ra
w/ DJ and Full Dance Floor

** No Cover Charge
Saturday, January 22, 2022
7 pm - 11 pm

at Maple Parlor
4870 K Street NE Washington DC 20017

Call Gregory Whitfield at (240) 555-0187 with questions.

```html
<!DOCTYPE html>
<html lang="en">
<head>
<meta charset="utf-8">
<title>Annual Holiday Celebration Flyer</title>
<link href="https://fonts.googleapis.com/css2?family=Oswald:wght@500;600;700&family=Montserrat:wght@400;700&family=Kaushan+Script&family=Allura&display=swap" rel="stylesheet">
<style>
  :root {
    --teal: #12848f;
    --teal-dark: #0b5f68;
    --teal-light: #3fb4c3;
    --gold: #d69a22;
    --gold-light: #f2c24f;
    --white: #ffffff;
    --ink: #1f2a2c;
  }
  * { margin: 0; padding: 0; box-sizing: border-box; }
  html, body { width: 1200px; height: 1200px; overflow: hidden; background: var(--white); }
  .flyer { position: relative; width: 1200px; height: 1200px; background: var(--white); overflow: hidden; font-family: "Oswald", sans-serif; }
  .flyer-shapes { position: absolute; inset: 0; }
  .abs { position: absolute; }

  .partner-marks { top: 92px; left: 0; width: 1200px; display: flex; justify-content: center; gap: 90px; }
  .partner-mark { display: flex; align-items: center; gap: 12px; font-family: "Oswald", sans-serif; font-weight: 600; font-size: 22px; color: var(--teal); text-transform: uppercase; }
  .partner-mark .dot-square { width: 26px; height: 26px; background: var(--teal); }
  .partner-mark .dot-circle { width: 28px; height: 28px; border-radius: 50%; background: var(--gold); }

  .presenters { top: 170px; width: 1200px; text-align: center; color: var(--teal); font-weight: 600; font-size: 31px; text-transform: uppercase; letter-spacing: 0.3px; }
  .present-our { top: 208px; width: 1200px; text-align: center; font-family: "Allura", cursive; color: var(--gold); font-size: 72px; line-height: 1; }
  .event-title { top: 268px; width: 1200px; text-align: center; text-transform: uppercase; font-weight: 700; line-height: 0.95;
    background: linear-gradient(180deg, #c98a17 0%, var(--gold-light) 60%, #c98a17 100%); -webkit-background-clip: text; background-clip: text; color: transparent; }
  .event-title .line-1 { display: block; font-size: 108px; }
  .event-title .line-2 { display: block; font-size: 84px; }
  .audience { top: 476px; width: 1200px; text-align: center; color: var(--gold); font-weight: 600; font-size: 32px; text-transform: uppercase; }
  .welcome { top: 510px; width: 1200px; text-align: center; font-family: "Kaushan Script", cursive; color: var(--teal); font-size: 112px; line-height: 1.1; }

  .brush-area { left: 0; top: 790px; width: 880px; height: 220px; background: linear-gradient(100deg, #c9a23a 0%, #f2d65c 45%, #d8a92c 100%); clip-path: polygon(6% 30%, 55% 8%, 92% 0, 100% 40%, 80% 100%, 0 100%, 0 55%); }
  .chef-photo { left: 400px; top: 660px; width: 380px; height: 440px; border-radius: 180px 180px 0 0; background: linear-gradient(180deg, #7a5a44 0%, #d9d4cc 45%, #bcb6ad 100%); }

  .event-date { top: 690px; left: 760px; width: 380px; text-align: center; color: var(--teal); font-style: italic; font-weight: 600; font-size: 66px; line-height: 1.02; text-transform: uppercase; letter-spacing: -1px; }

  .info-box { background: linear-gradient(90deg, var(--teal-dark), var(--teal)); color: var(--white); border-radius: 14px; }
  .venue { left: 70px; top: 960px; width: 470px; height: 120px; padding: 20px 32px; font-family: "Montserrat", sans-serif; }
  .venue .venue-name { font-weight: 700; font-size: 25px; text-transform: uppercase; }
  .venue .venue-address { font-size: 17px; line-height: 1.45; margin-top: 6px; text-transform: uppercase; letter-spacing: 0.5px; }
  .catering { left: 735px; top: 925px; width: 490px; height: 66px; padding: 9px 24px; font-family: "Montserrat", sans-serif; border-radius: 14px 0 0 14px; }
  .catering .chef { font-weight: 700; font-size: 20px; text-transform: uppercase; }
  .catering .extras { font-size: 16px; text-transform: uppercase; letter-spacing: 0.5px; }
  .admission { left: 735px; top: 1003px; width: 490px; height: 100px; padding: 8px 30px; text-align: right; font-weight: 600; font-size: 34px; line-height: 1.3; text-transform: uppercase; border-radius: 14px 0 0 14px; }

  .contact { top: 1132px; width: 1200px; text-align: center; color: var(--gold-light); font-weight: 600; font-size: 31px; text-transform: uppercase; }
</style>
</head>
<body>
<main class="flyer">
  <svg class="flyer-shapes" width="1200" height="1200" viewBox="0 0 1200 1200" aria-hidden="true">
    <defs>
      <linearGradient id="band" x1="0" y1="0" x2="1" y2="0">
        <stop offset="0" stop-color="#0e7480"/><stop offset="0.5" stop-color="#4bb9c6"/><stop offset="1" stop-color="#0e7480"/>
      </linearGradient>
      <linearGradient id="base" x1="0" y1="0" x2="0" y2="1">
        <stop offset="0" stop-color="#1aa0ae"/><stop offset="1" stop-color="#0b5f68"/>
      </linearGradient>
    </defs>
    <polygon points="0,0 1200,0 1200,30 740,50 500,28 200,62 0,45" fill="url(#band)"/>
    <polygon points="400,0 640,0 500,30" fill="#2a9eab" opacity="0.7"/>
    <polygon points="0,930 520,1000 1200,860 1200,1200 0,1200" fill="url(#base)"/>
    <polygon points="0,1080 760,1150 1200,1080 1200,1200 0,1200" fill="#0b5f68" opacity="0.6"/>
  </svg>

  <div class="abs brush-area" role="img" aria-label="Gold paint brush stroke decoration"></div>
  <div class="abs chef-photo" role="img" aria-label="Photo of the caterer, a smiling chef in a white chef's coat"></div>

  <div class="abs partner-marks">
    <div class="partner-mark"><span class="dot-square"></span>Pinecrest Harbor Realty Group</div>
    <div class="partner-mark"><span class="dot-circle"></span>Bluewater Lending Services, Inc.</div>
  </div>

  <h2 class="abs presenters">Pinecrest Harbor Realty Group &amp; Bluewater Lending Services, Inc.</h2>
  <p class="abs present-our">Present Our</p>
  <h1 class="abs event-title"><span class="line-1">Annual Holiday</span><span class="line-2">Celebration</span></h1>
  <p class="abs audience">For Agents, Originators, Clients &amp; Friends</p>
  <p class="abs welcome">All Are Welcome!!</p>

  <p class="abs event-date">Saturday,<br>January 22<br>2022</p>

  <div class="abs info-box venue">
    <p class="venue-name">At Maple Parlor</p>
    <p class="venue-address">4870 K Street NE<br>Washington DC 20017</p>
  </div>
  <div class="abs info-box catering">
    <p class="chef">Catered by Chef Ra Ra</p>
    <p class="extras">w/ DJ and Full Dance Floor</p>
  </div>
  <div class="abs info-box admission">
    <p>** No Cover Charge</p>
    <p>7 PM - 11 PM</p>
  </div>

  <p class="abs contact">Call Gregory Whitfield at (240) 555-0187 with questions.</p>
</main>
</body>
</html>
```